Business card for Mortgage broker business

I have already had the logo designed and am needing a great looking business card. My business focus is on servicing clients who may not be able to obtain finance through traditional lenders due to bad credit, short term employment or they just don't fit the banks profile. It needs to be professional, trust worthy but also have a caring fell about it.
I have provided files showing the green and black logo, the white logo(on white background so the file looks blank) and also a file with the white logo with a background of leaves that was made up which will probably be used for a website header.

Industry/Entity Type

Finance

Contact Information for Business Card

Marcus Dolbey
Managing Director, Accredited Finance Broker(AFB)
Po Box 287, Pakenham VIC 3810
marcus@kestrelfinance.com.au
www.kestrelfinance.com.au
0438 162 507

Requirements
Nice to have
• I have added a picture of myself as I would like to see some designs with the pic in it, but I'm not sure if I want it on there with the logo's or just the logo's

```html
<!DOCTYPE html>
<html lang="en">
<head>
<meta charset="utf-8">
<title>Kestrel Finance – Business Card</title>
<link rel="stylesheet" href="https://fonts.googleapis.com/css2?family=Montserrat:wght@400;500;700&display=swap">
<style>
  :root {
    --page-bg: #e9e9e7;
    --card-white: #ffffff;
    --brand-green: #1a6b3a;
    --ink: #2b2b2b;
    --ink-soft: #444444;
    --divider: #9a9a9a;
    --leaf-dark: #2a1a10;
    --leaf-brown: #6b3a1c;
    --leaf-orange: #b8692a;
    --leaf-green: #5e6a2a;
    --leaf-red: #4a1612;
    --suit-dark: #2a2422;
    --logo-grey: #d9d9d9;
    --card-shadow: 0 14px 30px rgba(0,0,0,0.25);
  }
  * { box-sizing: border-box; margin: 0; padding: 0; }
  html, body {
    width: 1200px; height: 900px; overflow: hidden;
    background: var(--page-bg);
    font-family: "Montserrat", Arial, sans-serif;
  }
  .canvas { position: relative; width: 1200px; height: 900px; }

  .card {
    position: absolute;
    width: 560px; height: 320px;
    border-radius: 22px;
    overflow: hidden;
    box-shadow: var(--card-shadow);
  }

  /* Front */
  .card-front { left: 70px; top: 90px; }
  .front-backdrop {
    position: absolute; inset: 0;
    background:
      radial-gradient(circle at 25% 20%, var(--leaf-orange) 0%, transparent 40%),
      radial-gradient(circle at 45% 55%, var(--leaf-green) 0%, transparent 45%),
      radial-gradient(circle at 90% 15%, var(--leaf-red) 0%, transparent 40%),
      linear-gradient(135deg, var(--leaf-brown) 0%, var(--leaf-dark) 100%);
  }
  .front-portrait {
    position: absolute; right: 0; top: 40px;
    width: 240px; height: 280px;
    background: linear-gradient(180deg, #8a6a55 0%, #6d4f3f 45%, var(--suit-dark) 60%, var(--suit-dark) 100%);
    border-top-left-radius: 120px 110px;
  }
  .front-web {
    position: absolute; left: 70px; top: 158px;
    font-size: 13px; font-weight: 500; color: #f2f2f2;
    letter-spacing: 0.3px;
  }
  .front-brand {
    position: absolute; left: 95px; top: 196px;
    color: var(--logo-grey); font-weight: 500;
    display: flex; flex-direction: column; align-items: flex-start;
  }
  .front-brand .brand-name { font-size: 50px; line-height: 1; letter-spacing: 1px; }
  .front-brand .brand-sub { font-size: 18px; letter-spacing: 10px; margin: 6px 0 0 70px; }

  /* Back */
  .card-back { left: 570px; top: 490px; background: var(--card-white); }
  .back-brand {
    position: absolute; left: 40px; top: 120px;
    color: var(--brand-green); font-weight: 700;
    display: flex; flex-direction: column;
  }
  .back-brand .brand-row { display: flex; align-items: center; gap: 8px; }
  .back-brand .brand-dot { width: 12px; height: 12px; border-radius: 50%; background: var(--brand-green); }
  .back-brand .brand-name { font-size: 40px; line-height: 1; }
  .back-brand .brand-sub { font-size: 13px; letter-spacing: 9px; margin: 6px 0 0 58px; }

  .back-divider {
    position: absolute; left: 262px; top: 42px;
    width: 1px; height: 236px;
    background: linear-gradient(180deg, transparent, var(--divider) 15%, var(--divider) 85%, transparent);
  }
  .contact {
    position: absolute; left: 282px; top: 56px;
    color: var(--ink-soft); font-size: 13px; line-height: 1.32;
  }
  .contact .name { color: var(--brand-green); font-weight: 700; font-size: 22px; line-height: 1.1; margin-bottom: 2px; }
  .contact .block { margin-bottom: 8px; }
  .contact .line { display: flex; align-items: center; gap: 8px; }
  .contact svg { width: 11px; height: 11px; flex: none; }
  .contact .web-strong { color: var(--brand-green); font-weight: 700; }
</style>
</head>
<body>
<main class="canvas">

  <section class="card card-front" aria-label="Business card front">
    <div class="front-backdrop" role="img" aria-label="Blurred autumn leaves background in orange, brown and green"></div>
    <div class="front-portrait" role="img" aria-label="Portrait photo of the managing director in a dark suit"></div>
    <p class="front-web">www.kestrelfinance.com.au</p>
    <div class="front-brand">
      <span class="brand-name">Kestrel</span>
      <span class="brand-sub">FINANCE</span>
    </div>
  </section>

  <section class="card card-back" aria-label="Business card back">
    <div class="back-brand">
      <div class="brand-row">
        <span class="brand-dot"></span>
        <span class="brand-name">Kestrel</span>
      </div>
      <span class="brand-sub">FINANCE</span>
    </div>

    <div class="back-divider"></div>

    <div class="contact">
      <p class="name">Marcus Dolbey</p>
      <div class="block">
        <p>Managing Director</p>
        <p>Accredited Finance Broker(AFB)</p>
      </div>
      <div class="block">
        <p>Po Box 287</p>
        <p>Brambleton VIC 3812</p>
      </div>
      <p class="line">
        <svg viewBox="0 0 12 12" aria-hidden="true"><path d="M2.5 1 L4.5 1 L5 3.5 L3.8 4.4 Q5 7 7.6 8.2 L8.5 7 L11 7.5 L11 9.5 Q11 11 9.5 11 Q1 10 1 2.5 Q1 1 2.5 1 Z" fill="var(--brand-green)"/></svg>
        0438 162 507
      </p>
      <p class="line">
        <svg viewBox="0 0 12 12" aria-hidden="true"><rect x="1" y="2.5" width="10" height="7" fill="none" stroke="var(--brand-green)" stroke-width="1.2"/><path d="M1 2.5 L6 6.5 L11 2.5" fill="none" stroke="var(--brand-green)" stroke-width="1.2"/></svg>
        marcus@kestrelfinance.com.au
      </p>
      <p class="line">
        <svg viewBox="0 0 12 12" aria-hidden="true"><circle cx="6" cy="6" r="5" fill="none" stroke="var(--brand-green)" stroke-width="1.2"/><path d="M1 6 H11 M6 1 Q3 6 6 11 M6 1 Q9 6 6 11" fill="none" stroke="var(--brand-green)" stroke-width="1"/></svg>
        <span>www.<span class="web-strong">kestrelfinance</span>.com.au</span>
      </p>
    </div>
  </section>

</main>
</body>
</html>
```